Car rental website design for a UAE car rental company

This project is about creating a new website design for a car rental company located in Dubai (United Arab Emirates), I opened the same project a few months ago but I didn't receive a lot of appealing entries so I closed it but this time I am marking the project as guaranteed to avoid such situation again, if you have already provided a design before then please re-submit again on this project so that it is considered while reviewing all the designs

A few important things:

1- We need a simple non-complex design
2- The final deliverable would be 2 screens (PSD, JPEG ... etc), the first screen is for the home page and the second screen is for an internal page
3- The home page must have a section that end users can use to rent a car online directly from the home page instead of going into some inner pages
4- The current website is very old and not very appealing so avoid creating a similar design (www.quarvin-drive.example)
5- The name is Quarvin but the company rents normal cars (no Limousin cars will be rented) so avoid adding any fancy cars in the images/graphics used in the design, just normal end users cars
6- The expected pages would be: home, About us, Our team, Strategy, Contact us and links to social media pages
7- The attachments include the company's logo and some screens from other car rental companies that provide online rentals/payments

If you have any questions please feel free to ask and please note that we will need the designs urgently

Thanks

Target Market(s)

Dubai - United Arab Emirates

Industry/Entity Type

It Company

Number of Pages Required

2 page

Font styles to use
Sans Serif

Requirements
Must have
• Check the project details
Nice to have
Should not have

```html
<!DOCTYPE html>
<html lang="en">
<head>
<meta charset="utf-8">
<title>Quarvin – Car Rental Dubai</title>
<link rel="stylesheet" href="https://fonts.googleapis.com/css2?family=Oswald:wght@500;700&family=Roboto+Condensed:wght@400;700&family=Roboto:ital,wght@0,400;0,500;1,400&display=swap">
<style>
:root{
  --black:#000;
  --nav:#262626;
  --nav-active:#0a0a0a;
  --band:#343434;
  --light:#eeeeee;
  --white:#fff;
  --text-muted:#8a8a8a;
  --text-dark:#444;
  --title-dim:#3a3a3a;
  --title-dim2:#555;
  --rule:#e2e2e2;
  --field:#6e6e6e;
  --footer:#3d3d3d;
  --accent:#b8202c;
}
*{margin:0;padding:0;box-sizing:border-box}
html,body{width:1200px;height:2590px;overflow:hidden;background:var(--black)}
body{font-family:"Roboto",Arial,sans-serif;color:var(--white);position:relative}

/* header */
.site-header{position:absolute;left:0;top:0;width:1200px;height:121px;background:var(--black)}
.brand{position:absolute;left:78px;top:38px;display:flex;align-items:center;gap:12px}
.brand-mark{width:34px;height:34px;background:var(--accent)}
.brand-name{font-family:"Roboto Condensed",sans-serif;font-size:30px;font-weight:400;color:#e6e6e6}
.hotline{position:absolute;left:866px;top:44px;display:flex;align-items:center;gap:14px}
.hotline-number{font-family:"Roboto Condensed",sans-serif;font-weight:700;font-size:29px;color:#ddd;letter-spacing:.5px}

/* nav */
.main-nav{position:absolute;left:0;top:121px;width:1200px;height:52px;background:var(--nav);border-bottom:1px solid #111;display:flex;padding-left:86px}
.main-nav a{display:block;height:52px;line-height:52px;padding:0 29px;font-size:12px;color:#d8d8d8;text-decoration:none;font-family:"Roboto Condensed",sans-serif;letter-spacing:.2px}
.main-nav a.active{background:var(--nav-active);color:#fff;border-bottom:3px solid #555}

/* hero */
.hero{position:absolute;left:0;top:173px;width:1200px;height:362px;background:linear-gradient(#050505 0%,#111 40%,#3a3a3a 41%,#8a8a8a 100%)}
.hero-photo{position:absolute;left:90px;top:80px;width:1010px;height:282px;background:radial-gradient(ellipse 50% 45% at 45% 55%,#4a4a4a 0%,#1e1e1e 60%,rgba(10,10,10,0) 100%)}
.hero-panel{position:absolute;left:642px;top:86px;width:473px;height:276px;background:rgba(20,20,20,.75)}
.hero-title{position:absolute;left:34px;top:24px;font-family:"Oswald",sans-serif;font-weight:700;font-size:38px;color:#fff;letter-spacing:.3px}
.hero-text{position:absolute;left:36px;top:82px;width:420px;font-size:11px;line-height:17px;color:#cfcfcf;text-transform:uppercase}
.btn-outline{position:absolute;border:1px solid #bbb;color:#fff;font-size:11px;text-align:center;font-family:"Roboto Condensed",sans-serif;background:#0c0c0c}
.btn-reserve{position:absolute;left:36px;top:190px;width:263px;height:46px;line-height:46px;text-align:center;background:linear-gradient(#f2f2f2,#9c9c9c);color:#333;font-family:"Roboto Condensed",sans-serif;font-size:21px;border-radius:3px}
.slider-arrow{position:absolute;left:1103px;width:24px;height:26px;background:#fff;display:flex;align-items:center;justify-content:center}

/* features */
.features{position:absolute;left:0;top:535px;width:1200px;height:375px;background:var(--white)}
.feature{position:absolute;top:0;width:313px}
.feature h3{position:absolute;top:50px;font-family:"Roboto Condensed",sans-serif;font-weight:400;font-size:20px;color:var(--text-dark)}
.feature .rule{position:absolute;top:83px;width:313px;height:4px;background:var(--rule)}
.feature .photo{position:absolute;top:99px;width:313px;height:98px}
.feature p{position:absolute;top:216px;width:313px;font-size:12px;line-height:18px;color:var(--text-muted)}
.feature .more{position:absolute;top:300px;font-size:12px;color:#333}
.btn-dark{position:absolute;top:287px;width:124px;height:33px;line-height:33px;background:#444;color:#fff;font-family:"Roboto Condensed",sans-serif;font-size:14px;text-align:center;border-radius:2px}

/* about / services */
.section-title{position:absolute;left:0;width:1200px;text-align:center;font-family:"Oswald",sans-serif;font-weight:700;font-size:38px}
.about{position:absolute;left:0;top:910px;width:1200px;height:287px;background:var(--black)}
.center-copy{position:absolute;left:170px;width:860px;text-align:center;font-size:13.5px;line-height:23px;color:#eee}
.services{position:absolute;left:0;top:1197px;width:1200px;height:443px;background:var(--band)}
.services h4{position:absolute;left:0;width:1200px;text-align:center;font-family:"Roboto Condensed",sans-serif;font-weight:700;font-size:25px;line-height:31px;color:#fff}
.service-list{position:absolute;left:0;top:266px;width:1200px;list-style:none;text-align:center;font-size:14px;line-height:26px;color:#fff}

/* testimonials */
.testimonials{position:absolute;left:0;top:1640px;width:1200px;height:313px;background:var(--light)}
.testimonials h2{position:absolute;left:0;top:30px;width:1200px;text-align:center;font-family:"Roboto Condensed",sans-serif;font-weight:400;font-size:25px;color:var(--text-dark)}
.avatar{position:absolute;left:245px;top:109px;width:142px;height:142px;border-radius:50%;border:6px solid #fff;box-shadow:0 0 0 1px #ccc;background:radial-gradient(circle at 50% 40%,#c9b7a6,#5b5f6a 70%,#3b3f48)}
.quote-mark{position:absolute;left:408px;top:120px;font-size:30px;color:#999;font-family:Georgia,serif}
.quote{position:absolute;left:428px;top:130px;width:525px;font-style:italic;font-size:13px;line-height:19px;color:#999}
.quote-author{position:absolute;left:428px;top:226px;font-style:italic;font-size:13px;color:#666}
.t-arrow{position:absolute;top:162px}

/* reservation */
.reservation{position:absolute;left:0;top:1953px;width:1200px;height:473px;background:var(--black);overflow:hidden}
.reservation-photo{position:absolute;left:215px;top:62px;width:800px;height:400px;background:radial-gradient(ellipse 50% 48% at 50% 55%,#2e2e2e 0%,#141414 60%,rgba(0,0,0,0) 100%)}
.reservation h2{position:absolute;left:0;top:45px;width:1200px;text-align:center;font-family:"Roboto Condensed",sans-serif;font-weight:400;font-size:24px;color:#fff}
.field{position:absolute;left:0;width:1200px;height:30px}
.field label{position:absolute;right:718px;top:7px;font-family:"Roboto Condensed",sans-serif;font-size:14px;color:#e6e6e6;text-transform:uppercase}
.field .input{position:absolute;left:508px;top:0;width:283px;height:30px;background:var(--field);opacity:.9;font-size:10px;color:#aaa;line-height:30px;padding-left:14px}
.submit{position:absolute;left:508px;top:400px;width:283px;height:30px;line-height:30px;text-align:center;background:#1b1b1b;border:1px solid #444;font-family:"Roboto Condensed",sans-serif;font-size:13px;color:#fff}

/* footer */
.site-footer{position:absolute;left:0;top:2426px;width:1200px;height:164px;background:var(--footer)}
.footer-links{position:absolute;left:0;top:40px;width:1200px;text-align:center;font-size:11px;color:#bbb;letter-spacing:.2px}
.copyright{position:absolute;left:0;top:70px;width:1200px;text-align:center;font-size:11px;color:#999}
.socials{position:absolute;left:528px;top:103px;display:flex;gap:8px}
.socials span{display:block;width:32px;height:32px;border-radius:50%;background:#d6d6d6;border:2px solid #888}
</style>
</head>
<body>

<header class="site-header">
  <div class="brand"><span class="brand-mark"></span><span class="brand-name">Quarvin</span></div>
  <div class="hotline">
    <svg width="36" height="36" viewBox="0 0 36 36" aria-hidden="true">
      <circle cx="18" cy="18" r="15" fill="none" stroke="#bbb" stroke-width="2.5"/>
      <path d="M12 11c2-1 3 0 4 2l-1 2c1 2 2 3 4 4l2-1c2 1 3 2 2 4-2 2-6 1-9-2s-5-7-2-9z" fill="#bbb"/>
    </svg>
    <span class="hotline-number">555 014 2290</span>
  </div>
</header>

<nav class="main-nav">
  <a class="active">HOME</a>
  <a>ABOUT US</a>
  <a>OUR TEAM</a>
  <a>STRATEGY</a>
  <a>OUR FLEET</a>
  <a>ONLINE RENTAL</a>
  <a>CONTACT US</a>
</nav>

<section class="hero">
  <div class="hero-photo" role="img" aria-label="Everyday family sedan shown in side profile"></div>
  <div class="hero-panel">
    <h1 class="hero-title">A SIMPLE CAR RENTAL</h1>
    <p class="hero-text">Quarvin has rented reliable everyday cars across Dubai since 2010. Book online in minutes and pick up your car today</p>
    <div class="btn-outline" style="left:36px;top:128px;width:101px;height:30px;line-height:28px">KNOW MORE</div>
    <div class="btn-reserve">RENT A CAR NOW</div>
  </div>
  <div class="slider-arrow" style="top:273px"><svg width="10" height="14" viewBox="0 0 10 14"><path d="M3 2l5 5-5 5" fill="none" stroke="#333" stroke-width="1.5"/></svg></div>
  <div class="slider-arrow" style="top:307px"><svg width="10" height="14" viewBox="0 0 10 14"><path d="M7 2L2 7l5 5" fill="none" stroke="#333" stroke-width="1.5"/></svg></div>
</section>

<section class="features">
  <article class="feature" style="left:86px">
    <h3>ECONOMY CARS</h3><div class="rule"></div>
    <div class="photo" role="img" aria-label="Compact hatchback parked on a Dubai street" style="background:linear-gradient(120deg,#8a9aa8,#d8dde2 45%,#a9b4bd 60%,#5c6670)"></div>
    <p>Quarvin offers a wide range of compact and economy cars for daily driving in Dubai. Low fuel use, easy parking and full insurance included in every rental!</p>
    <span class="more">Read More</span>
  </article>
  <article class="feature" style="left:444px">
    <h3>FAIR DAILY RATES</h3><div class="rule"></div>
    <div class="photo" role="img" aria-label="Mid-size family sedan in a parking lot" style="background:linear-gradient(#c9ccd0,#6f747a 60%,#b5b8bc)"></div>
    <p>Quarvin is proud to offer daily, weekly and monthly rates with no hidden fees. Our sedans, SUVs and family vans are affordable and always ready for pick up.</p>
    <span class="more">More Info</span>
  </article>
  <article class="feature" style="left:803px">
    <h3>BOOK YOUR CAR!</h3><div class="rule"></div>
    <div class="photo" role="img" aria-label="Customer receiving car keys at a rental desk" style="background:linear-gradient(100deg,#6a5a48,#b49c80 40%,#5a6478 70%,#3a3a3a)"></div>
    <p>Choose your car, dates and pickup point right here on the home page. Pay online securely and collect your car at the airport or delivered to your door.</p>
    <div class="btn-dark">BOOK NOW</div>
  </article>
</section>

<section class="about">
  <h2 class="section-title" style="top:48px;color:var(--title-dim)">ABOUT US</h2>
  <p class="center-copy" style="top:107px">Quarvin was founded in 2010 in Dubai, United Arab Emirates. Father and son team Danny &amp; Owen Hale, along with a dedicated team of rental advisers, work toward one goal: to make renting a car in Dubai simple, fast and fairly priced. From airport pickups and hotel deliveries to long-term leases for residents, Quarvin is your one stop shop for a clean, reliable everyday car in the city.</p>
  <div class="btn-outline" style="left:549px;top:207px;width:102px;height:30px;line-height:28px">KNOW MORE</div>
</section>

<section class="services">
  <h2 class="section-title" style="top:45px;color:var(--title-dim2)">AVAILABLE SERVICES</h2>
  <p class="center-copy" style="top:127px;font-size:13px">We can meet all your car rental needs in Dubai. Whether you land at the airport, visit for business, explore the city with family or need a car for months, we deliver a clean, reliable car with clear prices and friendly support.</p>
  <h4 style="top:191px">You can depend on us for the following rental<br>services in Dubai</h4>
  <ul class="service-list">
    <li>Airport, Hotel &amp; Home Delivery</li>
    <li>Daily &amp; Weekly Rentals</li>
    <li>Monthly Leasing</li>
    <li>Online Booking &amp; Payment</li>
  </ul>
  <div class="btn-outline" style="left:549px;top:379px;width:102px;height:30px;line-height:28px;background:transparent">KNOW MORE</div>
</section>

<section class="testimonials">
  <h2>CLIENT TESTIMONIALS</h2>
  <svg class="t-arrow" style="left:128px" width="18" height="28" viewBox="0 0 18 28"><path d="M14 3L4 14l10 11" fill="none" stroke="#999" stroke-width="4"/></svg>
  <div class="avatar" role="img" aria-label="Client portrait"></div>
  <span class="quote-mark">“</span>
  <p class="quote">Booking took me two minutes on the home page and the car was waiting for me at the airport. The price was exactly what I was quoted, the car was spotless and the return was quick. I rent with Quarvin every time I come to Dubai now and I recommend them to all my colleagues and friends.</p>
  <p class="quote-author">- Leon Varga</p>
  <svg class="t-arrow" style="left:1050px" width="18" height="28" viewBox="0 0 18 28"><path d="M4 3l10 11L4 25" fill="none" stroke="#999" stroke-width="4"/></svg>
</section>

<section class="reservation">
  <div class="reservation-photo" role="img" aria-label="Everyday sedan front view in low light"></div>
  <h2>RENT A CAR ONLINE</h2>
  <div class="field" style="top:114px"><label>Pick up date</label><div class="input"><svg style="position:absolute;right:8px;top:8px" width="14" height="14" viewBox="0 0 14 14"><rect x="1" y="2" width="12" height="11" fill="none" stroke="#ccc"/><path d="M1 5h12M4 1v3M10 1v3" stroke="#ccc"/></svg></div></div>
  <div class="field" style="top:156px"><label>Return date</label><div class="input"><svg style="position:absolute;right:8px;top:8px" width="14" height="14" viewBox="0 0 14 14"><rect x="1" y="2" width="12" height="11" fill="none" stroke="#ccc"/><path d="M1 5h12M4 1v3M10 1v3" stroke="#ccc"/></svg></div></div>
  <div class="field" style="top:197px"><label>Car type</label><div class="input"></div></div>
  <div class="field" style="top:239px"><label>Pickup location</label><div class="input"></div></div>
  <div class="field" style="top:280px"><label>Phone</label><div class="input"></div></div>
  <div class="field" style="top:320px"><label>Email</label><div class="input"></div></div>
  <div class="field" style="top:361px"><label>Special requests</label><div class="input"></div></div>
  <div class="submit">SUBMIT</div>
</section>

<footer class="site-footer">
  <p class="footer-links">ABOUT US &nbsp;| &nbsp;OUR TEAM &nbsp;| &nbsp;STRATEGY &nbsp;| &nbsp;OUR FLEET &nbsp;| &nbsp;ONLINE RENTAL &nbsp;| &nbsp;CONTACT US</p>
  <p class="copyright">ALL RIGHTS RESERVED. COPYRIGHTS @ 2014</p>
  <div class="socials"><span></span><span></span><span></span><span></span></div>
</footer>

</body>
</html>
```